Need Amazing Website for Consulting Company

We need an amazing website design for a Human Resources Consulting Company. This will be geared towards a more professional crowd, but we don't want it to be overly corporate and stuffy: Just, clean and professional and amazing. Please use the video link below for further instruction.

http://clipvarn.example/t/kzQmPoLe7

Thank You.

PS Logo file has been attached.

Target Market(s)

The target marketing is small business owners who have employees. These owners cant afford an in-house HR person so they would hire this client to consult and do the work for them.

Industry/Entity Type

It Company

Font styles to use
Sans Serif

Requirements
Must have
• Please watch video:

Must have spot for video on homepage.
Nice to have
• Clean, professional, but not overly corporate, we want a personal and fun feel to this site a bit to separate them from all the other executive type sites. This site should have some LIFE to it and reflect a local brand that is doing great things.
Should not have
• Should not be just a corporate site, should not be overly stuffy, should not be overly boring.

```html
<!DOCTYPE html>
<html lang="en">
<head>
<meta charset="utf-8">
<title>Mesa Ridge HR Consulting</title>
<link rel="stylesheet" href="https://fonts.googleapis.com/css2?family=Open+Sans:wght@400;600;700&family=Carlito:wght@400;700&family=Ubuntu:wght@500;700&family=Satisfy&display=swap">
<style>
:root{
  --red:#b8142c;
  --red-dark:#9c0f22;
  --ink:#222;
  --text:#333;
  --btn:#5e5e5e;
  --page:#f1f1f1;
  --card:#fff;
}
*{box-sizing:border-box;margin:0;padding:0}
html,body{width:1071px;height:1200px;overflow:hidden}
body{position:relative;background:var(--page);font-family:"Open Sans",sans-serif;color:var(--text)}
.abs{position:absolute}
.header{left:0;top:0;width:1071px;height:129px;background:#fff}
.brand{left:99px;top:38px;width:146px;display:flex;align-items:center;gap:8px}
.brand-name{font:700 17px/1.15 "Open Sans",sans-serif;color:var(--ink);width:112px}
.brand-dot{flex:none;width:26px;height:26px;border-radius:50%;background:var(--red)}
.tagline{left:289px;top:66px;font:400 18px/1 "Open Sans",sans-serif;color:#333;letter-spacing:.3px}
.tagline em{font-family:"Satisfy",cursive;font-style:normal;font-size:21px}
.social-top{right:98px;top:45px;display:flex;gap:5px}
.social-top span{width:23px;height:23px;border-radius:50%;background:var(--red)}
.social-top span:nth-child(2){background:#7a7a7a}
.call{right:98px;top:80px;font:700 15px/1 "Open Sans",sans-serif;color:#111}
.call b{color:var(--red)}
.nav{left:0;top:129px;width:1071px;height:31px;background:linear-gradient(#c81a33,var(--red-dark))}
.nav ul{list-style:none;display:flex;margin-left:98px;height:31px}
.nav li{font:700 12.5px/31px "Open Sans",sans-serif;color:#fff;padding:0 10px;border-right:1px solid rgba(0,0,0,.2)}
.nav li:first-child{padding-left:0}
.nav li:last-child{border:0}
.hero{left:0;top:160px;width:1071px;height:325px;background:linear-gradient(90deg,#b9c79a 0%,#d9d4c4 30%,#d8c5b8 55%,#8a6a5a 72%,#c6b5ab 88%,#dfe0e6 100%)}
.video{left:99px;top:180px;width:415px;height:285px;background:var(--red)}
.video .play{position:absolute;left:180px;top:115px}
.video .bar{position:absolute;left:0;bottom:0;width:415px;height:23px;background:#111}
.hero-title{left:547px;top:229px;font:700 27px/1.05 "Ubuntu",sans-serif;color:#fff;text-shadow:0 1px 3px rgba(0,0,0,.45)}
.hero-text{left:548px;top:294px;width:400px;font:400 15.5px/22px "Open Sans",sans-serif;color:#fff;text-shadow:0 1px 2px rgba(0,0,0,.4)}
.hero-btn{left:548px;top:373px;width:147px;height:39px;background:#111;border-bottom:3px solid #444;border-radius:3px;color:#fff;font:400 17px/36px "Open Sans",sans-serif;text-align:center}
.card{background:var(--card);border-radius:3px;box-shadow:0 1px 3px rgba(0,0,0,.2)}
.service{top:534px;width:211px;height:225px}
.service .icon{position:absolute;left:67px;top:-35px;width:79px;height:79px;border-radius:50%;background:var(--red);display:flex;align-items:center;justify-content:center}
.service h2{position:absolute;left:19px;top:59px;font:700 15px/1 "Open Sans",sans-serif;color:#111}
.service p{position:absolute;left:20px;top:83px;width:182px;font:400 11px/19px "Carlito",sans-serif;color:#333}
.news p{line-height:17px}
.news .date{display:block;margin-bottom:7px}
.btn{position:absolute;background:var(--btn);color:#fff;font:400 11.5px/23px "Carlito",sans-serif;padding:0 10px;border-radius:2px}
.service .btn{left:21px;top:187px}
.about{left:99px;top:773px;width:652px;height:233px}
.about h2,.enquire h2{position:absolute;left:19px;top:18px;font:700 15px/1 "Open Sans",sans-serif;color:#111}
.about p{position:absolute;left:19px;width:605px;font:400 11px/19px "Carlito",sans-serif}
.about .btn{left:20px;top:194px}
.enquire{left:762px;top:773px;width:211px;height:233px}
.field{position:absolute;left:18px;width:173px;height:23px;border:1px solid #d6d6d6;border-radius:3px;background:linear-gradient(#fff,#f3f3f3);font-size:9px;line-height:21px;padding-left:10px;color:#888}
.field.query{height:70px;line-height:1;padding-top:10px}
.go{position:absolute;left:148px;top:164px;width:34px;height:34px;border-radius:50%;background:var(--red);color:#fff;font:700 13px/34px "Open Sans",sans-serif;text-align:center}
.footer{left:0;top:1027px;width:1071px;height:141px;border-top:2px solid #e0e0e0;background:#f5f5f5}
.fhead{position:absolute;font:700 12px/1 "Open Sans",sans-serif;color:#444}
.flist{position:absolute;list-style:none;font:400 11.5px/20.6px "Carlito",sans-serif;color:#444}
.social-foot{left:823px;top:1061px;display:flex;gap:5px}
.social-foot span{width:34px;height:34px;border-radius:50%;background:var(--red)}
.social-foot span:nth-child(even){background:#6b6b6b}
.copy{left:0;top:1168px;width:1071px;height:32px;background:#ececec;border-top:1px solid #ddd;font:400 9.5px/30px "Carlito",sans-serif;text-align:center;color:#444}
</style>
</head>
<body>

<header class="abs header">
  <div class="abs brand"><span class="brand-name">Mesa Ridge HR Consulting</span><span class="brand-dot"></span></div>
  <div class="abs tagline">EFFECTIVE. <em>Experienced.</em> EFFICIENT</div>
  <div class="abs social-top" aria-label="Social links"><span></span><span></span><span></span></div>
  <div class="abs call">CALL NOW! <b>(505) 555-0148</b></div>
</header>

<nav class="abs nav">
  <ul><li>HOME</li><li>ABOUT US</li><li>SERVICES</li><li>RECRUITMENT</li><li>CONSULTANCY</li><li>CONTACT US</li></ul>
</nav>

<section class="abs hero" role="img" aria-label="Softly blurred photo of a smiling professional woman"></section>

<div class="abs video" aria-label="Video player">
  <svg class="play" width="55" height="55" viewBox="0 0 55 55"><circle cx="27.5" cy="27.5" r="24.5" fill="none" stroke="#fff" stroke-width="5"/><path d="M21 16 L38 27.5 L21 39Z" fill="#fff"/></svg>
  <svg class="bar" width="415" height="23" viewBox="0 0 415 23">
    <path d="M14 6 L24 11.5 L14 17Z" fill="#fff"/>
    <rect x="41" y="8" width="324" height="8" fill="#fff"/><rect x="41" y="8" width="41" height="8" fill="#999"/>
    <rect x="389" y="5" width="11" height="9" fill="none" stroke="#ccc" stroke-width="1.5"/><rect x="395" y="10" width="9" height="7" fill="none" stroke="#ccc" stroke-width="1.5"/>
  </svg>
</div>

<h1 class="abs hero-title">Human Resources<br>Consulting</h1>
<p class="abs hero-text">Lorem Ipsum is simply dummy text of the printing and typesetting industry. Lorem Ipsum has been the industry's standard dummy text ever since the 1500s</p>
<div class="abs hero-btn">Learn More</div>

<article class="abs card service" style="left:99px">
  <div class="icon"><svg width="40" height="40" viewBox="0 0 40 40" fill="#fff"><circle cx="16" cy="10" r="7"/><path d="M3 36 C3 24 9 20 16 20 C20 20 22 21 24 23 L24 36Z"/><circle cx="29" cy="28" r="6" fill="none" stroke="#fff" stroke-width="2.5"/><path d="M29 19v5M29 32v5M20 28h5M33 28h5" stroke="#fff" stroke-width="2.5"/></svg></div>
  <h2>RECRUITMENT</h2>
  <p>Lorem Ipsum is simply dummy text of the printing and typesetting industry. Lorem Ipsum has been the industry's standard dummy text ever since the 1500s</p>
  <span class="btn">Learn More</span>
</article>

<article class="abs card service" style="left:320px">
  <div class="icon"><svg width="42" height="40" viewBox="0 0 42 40"><path d="M21 4 C10 4 4 10 4 18 C4 26 11 31 21 31 C25 31 28 30 30 29 L38 36 L34 27 C37 25 38 22 38 18 C38 10 32 4 21 4Z" fill="none" stroke="#fff" stroke-width="3.5"/><circle cx="14" cy="18" r="2.6" fill="#fff"/><circle cx="21" cy="18" r="2.6" fill="#fff"/><circle cx="28" cy="18" r="2.6" fill="#fff"/></svg></div>
  <h2>CONSULTANCY</h2>
  <p>Lorem Ipsum is simply dummy text of the printing and typesetting industry. Lorem Ipsum has been the industry's standard dummy text ever since the 1500s</p>
  <span class="btn">Learn More</span>
</article>

<article class="abs card service" style="left:541px">
  <div class="icon"><svg width="44" height="34" viewBox="0 0 44 34" fill="#fff"><circle cx="9" cy="9" r="5"/><circle cx="35" cy="9" r="5"/><circle cx="22" cy="8" r="6.5"/><path d="M1 28 C1 19 5 16 9 16 C12 16 13 17 14 18 L14 28Z"/><path d="M43 28 C43 19 39 16 35 16 C32 16 31 17 30 18 L30 28Z"/><path d="M12 32 C12 21 17 17 22 17 C27 17 32 21 32 32Z"/></svg></div>
  <h2>HUMAN RESOURCES</h2>
  <p>Lorem Ipsum is simply dummy text of the printing and typesetting industry. Lorem Ipsum has been the industry's standard dummy text ever since the 1500s</p>
  <span class="btn">Learn More</span>
</article>

<article class="abs card service news" style="left:762px">
  <div class="icon"><svg width="36" height="32" viewBox="0 0 36 32"><rect x="2" y="2" width="32" height="28" fill="none" stroke="#fff" stroke-width="3"/><rect x="7" y="8" width="22" height="4" fill="#fff"/><rect x="7" y="15" width="9" height="9" fill="#fff"/><rect x="19" y="15" width="10" height="2.5" fill="#fff"/><rect x="19" y="20" width="10" height="2.5" fill="#fff"/></svg></div>
  <h2>LATEST NEWS</h2>
  <p>Lorem Ipsum is simply dummy text of the printing and typesetting<span class="date">1/28/2014</span>Lorem Ipsum is simply dummy text<span class="date">1/28/2014</span></p>
  <span class="btn">Learn More</span>
</article>

<section class="abs card about">
  <h2>ABOUT US</h2>
  <p style="top:42px">Mesa Ridge HR Consulting , LLC. (MRHRC) is an experienced consulting agency that is committed to providing businesses with effective and efficient Human Resources support by developing partnerships to meet company’s individual needs. Lorem Ipsum is simply dummy text of the printing and typesetting industry. Lorem Ipsum has been the industry's standard dummy text ever since the 1500s</p>
  <p style="top:124px">Mesa Ridge HR Consulting , LLC. (MRHRC) is an experienced consulting agency that is committed to providing businesses with effective and efficient Human Resources support by developing partnerships to meet company’s individual needs. Lorem Ipsum is simply dummy text of the printing and typesetting industry.</p>
  <span class="btn">Learn More</span>
</section>

<section class="abs card enquire">
  <h2>ENQUIRE NOW</h2>
  <div class="field" style="top:47px">Name</div>
  <div class="field" style="top:80px">Email Address</div>
  <div class="field" style="top:112px">Phone Number</div>
  <div class="field query" style="top:145px">Query</div>
  <div class="go">GO</div>
</section>

<footer class="abs footer">
  <div class="fhead" style="left:99px;top:14px">ABOUT US</div>
  <ul class="flist" style="left:99px;top:30px"><li>Home</li><li>About Us</li><li>Services</li><li>Human Resources</li></ul>
  <ul class="flist" style="left:236px;top:30px"><li>Consultancy</li><li>Careers</li><li>Contact Us</li><li>Testimonials</li></ul>
  <ul class="flist" style="left:345px;top:30px"><li>Privacy Policy</li><li>Disclaimer</li></ul>
  <div class="fhead" style="left:502px;top:14px">KEEP IN TOUCH</div>
  <ul class="flist" style="left:502px;top:30px"><li>MRHRC, LLC.</li><li>P.O. Box 5520</li><li>Rio Verde, NM 87199</li><li>(505) 555-0148</li></ul>
  <div class="fhead" style="left:823px;top:14px">SOCIAL WITH US</div>
</footer>
<div class="abs social-foot" aria-label="Social links"><span></span><span></span><span></span><span></span></div>

<div class="abs copy">Copyright © 2014 Mesa Ridge HR Consulting. All rights reserved</div>

</body>
</html>
```